Need effective Landing Page for product and service

Need help re-designing landing page:

Our company (in New York) offers upgrades to homes to make them more efficient, save energy and reduce utility bills. We do not do, or suggest every possible measure, like sealing and insulating a home, replacing windows, etc. We only offer high efficiency Ductless Mini Split Systems.

The landing page is to introduce the idea, and get people to fill the form. We already running a page at www.coolnest-air.net, but it is dull and boring, while it must be exciting, creating an urge to fill the form (schedule live consultation).

Visitors get to the page from Facebook Ad, designer must make sure there is congruence between the ad and the page.

```html
<!DOCTYPE html>
<html lang="en">
<head>
<meta charset="utf-8">
<title>Brisaro Comfort – Ductless Heat &amp; Cool</title>
<link rel="stylesheet" href="https://fonts.googleapis.com/css2?family=Lato:wght@400;700&display=swap">
<style>
  :root {
    --navy-deep: #0b2449;
    --navy: #11366a;
    --navy-glow: #1d5290;
    --yellow: #ecc22f;
    --yellow-text: #f1c737;
    --ink: #17304f;
    --heading-blue: #244a72;
    --nav-muted: #8fb0d6;
    --body-muted: #7f9fc6;
    --white: #ffffff;
  }
  * { box-sizing: border-box; margin: 0; padding: 0; }
  html, body { width: 1200px; height: 900px; overflow: hidden; }
  body { font-family: "Lato", sans-serif; background: var(--white); position: relative; }

  .hero {
    position: absolute; left: 0; top: 0; width: 1200px; height: 477px;
    background: radial-gradient(ellipse 520px 380px at 880px 300px, var(--navy-glow) 0%, var(--navy) 45%, var(--navy-deep) 100%);
  }
  .brand {
    position: absolute; left: 126px; top: 22px; height: 68px; width: 158px;
    display: flex; align-items: center; gap: 8px;
  }
  .brand-mark { width: 14px; height: 14px; border-radius: 50%; background: var(--yellow); flex: none; }
  .brand-name { color: var(--yellow-text); font-weight: 700; font-size: 22px; }

  .main-nav {
    position: absolute; left: 512px; top: 0; width: 688px; height: 79px;
    border-bottom: 1px solid rgba(143,176,214,0.25);
    display: flex;
  }
  .main-nav a {
    display: block; height: 79px; padding-top: 49px;
    font-size: 14.5px; font-weight: 700; text-decoration: none;
    color: var(--nav-muted); margin-right: 24px;
  }
  .main-nav a:first-child { padding-left: 3px; padding-right: 6px; color: var(--white); border-bottom: 2px solid var(--white); }

  .hero-title { position: absolute; left: 130px; top: 136px; font-size: 44px; font-weight: 700; color: var(--yellow-text); }
  .hero-sub { position: absolute; left: 130px; top: 200px; width: 580px; font-size: 24px; line-height: 29px; color: var(--white); font-weight: 400; }
  .hero-copy { position: absolute; left: 130px; top: 282px; width: 470px; font-size: 13.2px; line-height: 20px; color: var(--body-muted); }

  .benefits {
    position: absolute; left: 0; top: 477px; width: 1200px; height: 176px; background: var(--yellow);
  }
  .benefit-list { position: absolute; left: 138px; top: 28px; list-style: none; }
  .benefit-list li {
    display: flex; align-items: center; gap: 15px; height: 36px;
    font-size: 17.5px; font-weight: 700; color: var(--ink);
  }
  .benefit-list svg { width: 34px; height: 34px; flex: none; }

  .product-visual {
    position: absolute; left: 700px; top: 180px; width: 345px; height: 400px;
    background: radial-gradient(ellipse at 55% 60%, #f4f6f8 0%, #dfe4ea 45%, rgba(223,228,234,0) 72%);
  }

  .value-title {
    position: absolute; left: 0; top: 690px; width: 1200px; text-align: center;
    font-size: 31px; font-weight: 700; color: var(--heading-blue);
  }
  .feature-photo { position: absolute; top: 763px; width: 300px; height: 137px; }
  .photo-home { left: 130px; background: linear-gradient(180deg, #3a8ee0 0%, #6fb1ee 55%, #4d7a3c 100%); }
  .photo-air { left: 449px; background: radial-gradient(ellipse at 50% 50%, #4aa3f2 0%, #1660b5 55%, #0b3f86 100%); }
  .photo-family { left: 770px; background: linear-gradient(180deg, #b9dcf5 0%, #d9b89e 60%, #c79a7c 100%); }
</style>
</head>
<body>
  <header class="hero">
    <div class="brand">
      <span class="brand-mark"></span>
      <span class="brand-name">Brisaro</span>
    </div>
    <nav class="main-nav">
      <a href="#">DUCTLESS A/C &amp; HEAT PUMPS</a>
      <a href="#">TESTIMONIALS</a>
      <a href="#">INSTALLATIONS</a>
      <a href="#">ABOUT US</a>
    </nav>
    <h1 class="hero-title">Is your Home Efficient?</h1>
    <h2 class="hero-sub">Become GREEN! Get High Efficiency Ductless HEAT and COOL System and Save Money</h2>
    <p class="hero-copy">Set yourself free from high energy costs. Create a more comfortable, energy-efficient home and cut your energy bills by hundreds, or even more every year by upgrading your home heating and cooling system.<br>Home heating and cooling expenses account for about 50% of total monthly energy bills. This was researched by several independent studies. Cutting energy bills by improving your home performance is one of the ways to become GREEN - save wasted resources and reduce environmental impact.</p>
  </header>

  <section class="benefits">
    <ul class="benefit-list">
      <li><svg viewBox="0 0 34 34"><circle cx="17" cy="17" r="15" fill="none" stroke="#17304f" stroke-width="2.5"/><path d="M10 17.5l5 5 9-10" fill="none" stroke="#17304f" stroke-width="3" stroke-linecap="round" stroke-linejoin="round"/></svg>Reduce wasted energy - heat pumps are 30% more efficient</li>
      <li><svg viewBox="0 0 34 34"><circle cx="17" cy="17" r="15" fill="none" stroke="#17304f" stroke-width="2.5"/><path d="M10 17.5l5 5 9-10" fill="none" stroke="#17304f" stroke-width="3" stroke-linecap="round" stroke-linejoin="round"/></svg>Improve the quality of air you and your family breathes</li>
      <li><svg viewBox="0 0 34 34"><circle cx="17" cy="17" r="15" fill="none" stroke="#17304f" stroke-width="2.5"/><path d="M10 17.5l5 5 9-10" fill="none" stroke="#17304f" stroke-width="3" stroke-linecap="round" stroke-linejoin="round"/></svg>Stop fighting over "who has the control"</li>
    </ul>
  </section>

  <div class="product-visual" role="img" aria-label="Two ductless indoor wall units, an outdoor inverter unit and a remote control"></div>

  <h2 class="value-title">Gain better control of your energy bills, improve comfort and health!</h2>
  <div class="feature-photo photo-home" role="img" aria-label="House under a sunny blue sky"></div>
  <div class="feature-photo photo-air" role="img" aria-label="Swirls of cool blue air"></div>
  <div class="feature-photo photo-family" role="img" aria-label="Happy family smiling together"></div>
</body>
</html>
```